Summit Iron Peaks Marketing Flyer

I need a 1 page flyer that will go in a magazine to advertise our youth sports club and the various sports we have teams for. I want to make sure we feature pictures of our teams, our logos for basketball and volleyball, our title logo from our website and most importantly, HOW TO CONTACT US by going to our website www.summitironpeaks-example.com

Target Market(s)

Youth Sports Club

Colors
85cae6

Requirements
Must have
• Use the colors from our website: Carolina blue, black and silver. Must use the info provided in the Word Document I provided. Must have in bold and enlarged lettering how to contact us by going to our website www.summitironpeaks-example.com

```html
<!DOCTYPE html>
<html lang="en">
<head>
<meta charset="utf-8">
<title>Summit Iron Peaks Flyer</title>
<link href="https://fonts.googleapis.com/css2?family=Graduate&family=Roboto+Slab:wght@800&display=swap" rel="stylesheet">
<style>
  :root {
    --carolina: #85cae6;
    --navy: #2e6583;
    --deep: #235670;
    --silver: #a8abae;
    --backdrop: #3a3a3c;
    --paper: #ffffff;
    --ink: #1b1b1b;
  }
  * { margin: 0; padding: 0; box-sizing: border-box; }
  html, body { width: 911px; height: 1200px; overflow: hidden; background: var(--backdrop); }
  .flyer {
    position: absolute; left: 76px; top: 64px; width: 759px; height: 1072px;
    background: var(--paper); overflow: hidden;
  }
  .masthead {
    position: absolute; left: 0; top: 0; width: 100%; height: 136px;
    background: var(--carolina);
    display: flex; align-items: center; justify-content: center;
  }
  .masthead h1 {
    font-family: "Graduate", serif; font-weight: 400;
    font-size: 54px; color: var(--navy); letter-spacing: 1px; white-space: nowrap;
  }
  .masthead-rule { position: absolute; left: 0; top: 136px; width: 100%; height: 10px; background: var(--navy); }
  .team-photo { position: absolute; left: 0; top: 146px; width: 759px; height: 410px; }
  .intro {
    position: absolute; left: 40px; top: 520px; width: 679px;
    font-family: "Graduate", serif; font-size: 14.5px; line-height: 20px;
    color: var(--navy); text-align: center; font-variant: small-caps; letter-spacing: .4px;
  }
  .tryouts {
    position: absolute; left: 36px; top: 630px; width: 686px; height: 174px;
    background: var(--navy); border-radius: 20px;
    font-family: "Roboto Slab", serif; font-weight: 800; color: var(--paper);
    font-size: 17.5px; letter-spacing: 1px; text-transform: uppercase;
  }
  .tryout-row { position: absolute; left: 0; width: 100%; display: flex; align-items: center; }
  .tryout-sport { width: 306px; text-align: right; padding-right: 28px; }
  .tryout-when { line-height: 21px; }
  .row-basketball { top: 28px; }
  .row-volleyball { top: 72px; }
  .row-softball { top: 126px; }
  .sponsors {
    position: absolute; left: 0; top: 850px; width: 100%; height: 80px;
    display: flex; align-items: center; justify-content: center; gap: 36px;
    font-family: "Graduate", serif;
  }
  .club-mark { display: flex; align-items: center; gap: 8px; font-size: 15px; color: var(--navy); }
  .club-mark .dot { width: 14px; height: 14px; border-radius: 50%; background: var(--carolina); }
  .partner-mark { font-size: 34px; color: var(--ink); }
  .contact {
    position: absolute; left: 0; top: 958px; width: 100%; height: 114px;
    background: var(--silver); text-align: center; font-family: "Graduate", serif; color: var(--navy);
  }
  .contact-lead { font-size: 22px; margin-top: 20px; font-variant: small-caps; letter-spacing: 1px; }
  .contact-url { font-size: 31px; margin-top: 6px; letter-spacing: .5px; }
</style>
</head>
<body>
<main class="flyer">
  <header class="masthead"><h1>SUMMIT IRON PEAKS</h1></header>
  <div class="masthead-rule"></div>

  <svg class="team-photo" viewBox="0 0 759 410" role="img" aria-label="Team photo: volleyball players in light blue and black uniforms wearing medals, standing in a gym">
    <defs>
      <linearGradient id="photo-tone" x1="0" y1="0" x2="0" y2="1">
        <stop offset="0" stop-color="#d9dde1"/>
        <stop offset=".45" stop-color="#8fbfd6"/>
        <stop offset=".8" stop-color="#3c4650"/>
        <stop offset="1" stop-color="#c79a6e"/>
      </linearGradient>
    </defs>
    <path d="M0 0H759V280Q380 360 0 280Z" fill="url(#photo-tone)"/>
    <path d="M0 280Q380 360 759 280" fill="none" stroke="var(--navy)" stroke-width="4"/>
  </svg>

  <p class="intro">Summit Iron Peaks is a Ridgeford, Utah based Basketball, Volleyball and Softball club youth sports program for both boys and girls 2nd – 12th grades. Teams range from Developmental to Premier Travel teams, so if you’re looking to improve your skills, we can help.</p>

  <section class="tryouts">
    <div class="tryout-row row-basketball"><span class="tryout-sport">Basketball tryouts:</span><span class="tryout-when">End of August</span></div>
    <div class="tryout-row row-volleyball"><span class="tryout-sport">Volleyball tryouts:</span><span class="tryout-when">October for Jr. High /<br>November for High School</span></div>
    <div class="tryout-row row-softball"><span class="tryout-sport">Softball tryouts:</span><span class="tryout-when">July</span></div>
  </section>

  <div class="sponsors">
    <span class="club-mark"><span class="dot"></span>Summit Iron Peaks</span>
    <span class="club-mark"><span class="dot"></span>Summit Iron Peaks</span>
    <span class="partner-mark">Playfield Hub</span>
  </div>

  <footer class="contact">
    <p class="contact-lead">For more information, please visit our website:</p>
    <p class="contact-url">WWW.SUMMITIRONPEAKS-EXAMPLE.COM</p>
  </footer>
</main>
</body>
</html>
```